Zielgruppe
Wir eröffnen einen neune Onlineshop rund um das Thema Gartengeräte, im Sinne von Schläuchen, Schlauchwagen, Gartenbewässerung, Blumenkästen und Co.
Aufgabenstellung
Wir benötigen für diesen Shop ein komplettes Design ( Header,Footer, Menü, Detailansicht, Buttons) welches wir nachher in unseren Kerbel Shop einbinden.
Das Template wird von uns erstellt.
Die farbliche Gestaltung sollte zum Thema passen, hier dürfen also gerne Blau und Grüntöne verwendet werden.
Es soll kein klassisches 3 Spaltenlayout sein, gerne würden wir mit einem 2 Spaltenlayout arbeiten, links mit der Kategoriespalte und dann eine große Produkt und Inhaltsspalte
Der Shop wird den Namen minaru tragen.

```html
<!DOCTYPE html>
<html lang="en">
<head>
<meta charset="utf-8">
<title>Minaru – Garden Shop</title>
<link href="https://fonts.googleapis.com/css2?family=Ubuntu:wght@400;500;700&display=swap" rel="stylesheet">
<style>
:root{
  --green:#8cc63e;
  --green-dark:#6fa82a;
  --blue:#3a8fd6;
  --dark:#3d3d3d;
  --text:#555;
  --muted:#888;
  --line:#dcdcdc;
  --pale:#f4f4f4;
  --footer:#eef6e0;
  --pink:#d94fd0;
  --white:#fff;
}
*{box-sizing:border-box;margin:0;padding:0}
html,body{width:808px;height:1200px;overflow:hidden}
body{position:relative;background:#fff;font-family:Arial,Helvetica,sans-serif;color:var(--text)}
.abs{position:absolute}
.deco-left{left:40px;top:0;width:70px;height:250px;background:linear-gradient(180deg,#9bd04a,#5aa02a 60%,#fff);border-radius:0 0 40px 40px;opacity:.8}
.deco-right{left:690px;top:0;width:80px;height:250px;background:linear-gradient(180deg,#a6d64e,#5aa02a 60%,#fff);border-radius:0 0 40px 40px;opacity:.8}
.grass{left:0;top:1150px;width:808px;height:50px;background:linear-gradient(180deg,#fff,#9fd15a 60%,#6fae2c)}
.page{left:107px;top:7px;width:583px;height:1180px;background:var(--white);box-shadow:0 0 6px rgba(0,0,0,.15)}
.logo{left:115px;top:8px;font-family:Ubuntu,sans-serif;font-size:28px;color:var(--green);letter-spacing:.5px}
.phone{left:400px;top:22px;font-size:12.5px;color:var(--green);display:flex;align-items:center;gap:4px}
.currency{left:544px;top:26px;font-size:6.5px;color:#777;display:flex;align-items:center;gap:5px}
.currency span.sel{border:1px solid #ccc;width:57px;height:10px;font-size:5.5px;padding:1px 3px;color:#999}
.flags{left:652px;top:26px;display:flex;gap:6px}
.flags i{display:block;width:10px;height:7px}
.nav{left:115px;top:49px;width:567px;height:25px;background:var(--green);display:flex;font-family:Ubuntu,sans-serif;font-weight:500;font-size:9px;color:#fff}
.nav a{display:flex;align-items:center;padding:0 11px;border-right:1px solid #7db533}
.nav .home{background:var(--blue);width:32px;justify-content:center;padding:0}
.cat-btn{left:115px;top:81px;width:117px;height:24px;background:var(--blue);color:#fff;font-family:Ubuntu,sans-serif;font-weight:700;font-size:8px;padding:7px 10px}
.search{left:244px;top:81px;width:264px;height:23px;border:1px solid var(--line);display:flex}
.search b{width:21px;background:var(--green);display:flex;align-items:center;justify-content:center}
.search span{font-size:7.5px;color:#aaa;padding:6px 0 0 26px}
.cart{left:520px;top:81px;width:162px;height:23px;background:var(--dark);color:#fff;font-size:8px;display:flex;align-items:center;padding:0 8px;gap:8px}
.cart small{font-size:6px}
.cat-list{left:115px;top:111px;width:117px;border:1px solid var(--line);list-style:none;font-family:Ubuntu,sans-serif;font-size:7.5px;color:#444}
.cat-list li{height:20.7px;line-height:20.7px;padding-left:10px;border-bottom:1px solid var(--line)}
.cat-list li:last-child{border-bottom:0}
.cat-list li.on{background:var(--green);color:#fff}
.why{left:115px;top:438px;width:117px;height:229px;background:#f6f8fb;border:1px solid #e4e8ee;padding:8px 7px;font-family:Ubuntu,sans-serif}
.why h3{font-size:8px;color:#222;font-weight:700}
.why h3 em{font-style:normal;color:var(--green);font-size:10px}
.badge{display:flex;align-items:center;gap:7px;margin-top:10px;font-family:Arial,sans-serif;font-size:5.5px;color:#888;line-height:1.4}
.badge i{width:22px;height:22px;border-radius:50%;background:#c9a640;flex:none}
.badge i.b{background:#4a5c7a}
.why p.acc{font-size:7.5px;color:#333;margin:12px 0 6px}
.pay-grid{display:flex;flex-wrap:wrap;gap:4px}
.pay-grid span{font-family:Ubuntu,sans-serif;font-weight:700;font-size:8px;color:#2c5ea8;background:#fff;border:1px solid #e0e0e0;height:20px;display:flex;align-items:center;justify-content:center;width:48px}
.pay-grid span.w{width:100px;color:#e07b20;font-size:11px;height:28px}
.promo-water{left:115px;top:684px;width:117px;height:228px;background:linear-gradient(160deg,#f3ede6,#d35a7a 55%,#3f6a2c)}
.promo-water .t{position:absolute;left:12px;top:155px;color:#fff;font-family:Ubuntu,sans-serif;font-weight:700;font-size:14.5px;line-height:1.25}
.promo-water .shop{position:absolute;left:55px;top:202px;width:62px;height:17px;background:rgba(110,168,42,.9);color:#fff;font-family:Ubuntu,sans-serif;font-weight:700;font-size:10px;text-align:center;line-height:17px}
.promo-ship{left:115px;top:930px;width:117px;height:105px;background:linear-gradient(135deg,#9fd24c,#6aa630);color:#fff;font-family:Ubuntu,sans-serif;padding:8px 10px}
.promo-ship .big{font-size:24px;font-weight:700;line-height:1}
.promo-ship .mid{font-size:14px;font-weight:700}
.promo-ship p{font-size:8px;line-height:1.25}
.hero{left:244px;top:113px;width:438px;height:182px;background:linear-gradient(180deg,#7ea05a,#4d7a2c 55%,#3c6a24)}
.dots{right:8px;bottom:9px;display:flex;gap:3px}
.dots i{width:5px;height:5px;border-radius:50%;background:#fff;display:block}
.sec-head{left:244px;width:438px;height:20px;background:var(--pale);border-bottom:2px solid #e6e6e6;font-family:Ubuntu,sans-serif;font-weight:500;font-size:8.5px;color:var(--green);padding:5px 12px}
.arrows{position:absolute;right:8px;top:5px;font-size:7px;color:#ccc;letter-spacing:6px}
.tile{top:340px;width:138px;height:149px}
.tile .img{height:107px}
.tile .cap{height:42px;padding:5px 6px;color:#fff;position:relative}
.tile h4{font-family:Ubuntu,sans-serif;font-weight:500;font-size:10px}
.tile p{font-size:5.7px;line-height:1.4;margin-top:1px}
.tile .go{position:absolute;right:6px;bottom:8px;width:10px;height:10px;border-radius:50%;background:#fff}
.card{width:138px}
.card .img{height:114px;border:1px solid var(--line);position:relative}
.price{position:absolute;right:0;bottom:0;background:var(--green);color:#fff;font-family:Ubuntu,sans-serif;height:18px;padding:0 5px;display:flex;align-items:baseline;gap:4px;font-size:11px;line-height:18px}
.price small{font-size:6px}
.price s{font-size:6px}
.card h5{font-weight:400;font-size:7px;color:var(--green);margin-top:8px}
.card p{font-size:6.2px;line-height:1.5;color:#888;margin-top:3px;letter-spacing:.2px}
.actions{display:flex;margin-top:8px}
.actions .add{width:63px;height:19px;background:var(--dark);color:#fff;font-family:Ubuntu,sans-serif;font-size:7px;text-align:center;line-height:19px}
.actions .add.on{background:var(--blue)}
.actions .ic{width:26px;height:19px;border:1px solid var(--line);margin-left:4px;display:flex;align-items:center;justify-content:center}
.actions .ic+.ic{margin-left:0;border-left:0}
.offer{left:244px;top:748px;width:438px;height:77px;border:1px solid var(--line);background:linear-gradient(180deg,#fff 70%,#a9d85e)}
.offer .art1{left:8px;top:6px;width:90px;height:60px;background:#c8a879;border-radius:6px}
.offer .art2{left:365px;top:12px;width:65px;height:50px;background:#b3a18a;border-radius:6px}
.offer h2{left:115px;top:22px;font-family:Ubuntu,sans-serif;font-weight:700;font-size:11.5px;color:#333}
.offer h2 em{font-style:normal;color:var(--green);font-size:14px}
.offer .sub{left:134px;top:45px;font-family:Ubuntu,sans-serif;font-size:6.8px;color:var(--blue)}
.offer .btn{left:276px;top:34px;width:74px;height:20px;background:var(--pink);color:#fff;font-family:Ubuntu,sans-serif;font-weight:500;font-size:8.5px;text-align:center;line-height:20px}
.footer{left:113px;top:1057px;width:570px;height:100px;background:var(--footer);font-family:Ubuntu,sans-serif}
.fcol{position:absolute;top:17px}
.fcol h6{font-size:8.5px;font-weight:500;color:var(--green);margin-bottom:5px}
.fcol li{list-style:none;font-size:6.2px;color:#555;line-height:12.6px}
.fcol li::before{content:"›› ";color:#888}
.fcol.social li::before{content:"";display:inline-block;width:9px;height:9px;border-radius:50%;background:#cfd7c6;margin-right:5px;vertical-align:middle}
.fcol.social li{line-height:16px}
.fcol.contact p{font-size:6.2px;color:#555;line-height:1.5;margin-bottom:5px}
.fcol.contact b{color:#333}
.bottom{left:113px;top:1157px;width:570px;height:21px;background:var(--green);color:#fff;font-family:Ubuntu,sans-serif;font-size:6.2px;padding:0 16px;display:flex;align-items:center;justify-content:space-between}
.bottom .pm{display:flex;gap:4px;align-items:center}
.bottom .pm b{background:#fff;color:#2c5ea8;font-size:5px;padding:2px 3px}
</style>
</head>
<body>
<div class="abs deco-left" role="img" aria-label="Climbing flowers and vines decoration"></div>
<div class="abs deco-right" role="img" aria-label="Climbing flowers, vines and a butterfly decoration"></div>
<div class="abs grass" role="img" aria-label="Fresh grass strip"></div>
<div class="abs page"></div>

<header>
  <div class="abs logo">Minaru</div>
  <div class="abs phone">
    <svg width="9" height="11" viewBox="0 0 9 11"><path d="M2 0l2 3-1 1.5c.6 1.5 1.6 2.7 3 3.5L7.3 7 9 9.5 7.5 11C4 10 1 6.5 0 2.5z" fill="#8cc63e"/></svg>
    +1 0555 0142 7788
  </div>
  <div class="abs currency">Currencies: <span class="sel">US Dollar ▾</span></div>
  <div class="abs flags"><i style="background:linear-gradient(#222 33%,#d00 33% 66%,#fc0 66%)"></i><i style="background:#2a3f8f;border:1px solid #d00"></i></div>
  <nav class="abs nav">
    <a class="home"><svg width="10" height="9" viewBox="0 0 10 9"><path d="M5 0l5 4.5H8.5V9H6V6H4v3H1.5V4.5H0z" fill="#fff"/></svg></a>
    <a>PRODUCTS</a><a>SERVICE</a><a>GARDEN TIPS</a><a>NEWS</a><a>Checkout</a><a>Log In</a>
  </nav>
  <div class="abs cat-btn">SHOP BY CATEGORY ▾</div>
  <div class="abs search">
    <b><svg width="8" height="8" viewBox="0 0 8 8"><circle cx="3.2" cy="3.2" r="2.4" stroke="#fff" stroke-width="1.2" fill="none"/><path d="M5 5l2.5 2.5" stroke="#fff" stroke-width="1.3"/></svg></b>
    <span>Tell us what you looking....</span>
  </div>
  <div class="abs cart">
    <svg width="16" height="14" viewBox="0 0 16 14"><path d="M1 2h3l2 9h8l2-7H5" stroke="#8cc63e" stroke-width="1.6" fill="none"/></svg>
    <span>Shopping Cart: <small>0 item(s)</small></span>
    <span style="margin-left:auto;font-size:7px">▼</span>
  </div>
</header>

<aside>
  <ul class="abs cat-list">
    <li class="on">Seed &amp; Fertilizer</li><li>Handsets</li><li>Manual shears</li><li>Motorized Garden Care</li><li>Lawn Mower</li><li>Expert</li><li>Blue Power</li><li>Lawn</li><li>Grove</li><li>Ground</li><li>Ice &amp; Snow</li><li>Edit</li><li>Maintain</li><li>Mowing</li><li>Electric</li>
  </ul>
  <div class="abs why">
    <h3>Why Buy From <em>Minaru</em></h3>
    <div class="badge"><i class="b"></i><span>Secure Shopping<br>Verified Stores certified</span></div>
    <div class="badge"><i></i><span>Secure Shopping<br>SSL Certified</span></div>
    <p class="acc">Also We Accept:</p>
    <div class="pay-grid">
      <span>Pelvanto</span><span>Crestiva</span><span>Ombrelo</span><span>Kartilo</span><span class="w">Sendrafo</span>
    </div>
  </div>
  <div class="abs promo-water" role="img" aria-label="Woman watering colourful garden flowers">
    <div class="t">Water Garden<br>Accesories</div>
    <div class="shop">Shop Now</div>
  </div>
  <div class="abs promo-ship">
    <div class="big">FREE</div>
    <div class="mid">SHIPPING</div>
    <p style="font-size:9px">On order over € 99</p>
    <p style="margin-top:6px">This offer is vaild on all<br>our store items</p>
  </div>
</aside>

<main>
  <div class="abs hero" role="img" aria-label="Gardeners mowing a lawn and tending flower beds by a wooden house">
    <div class="abs dots"><i></i><i></i><i></i><i></i><i></i></div>
  </div>

  <div class="abs sec-head" style="top:306px">TOP PROPDUCTS<span class="arrows">◀▶</span></div>
  <div class="abs tile" style="left:244px">
    <div class="img" role="img" aria-label="Red lawn mower on grass" style="background:linear-gradient(135deg,#7aa84a,#b9403a 70%,#444)"></div>
    <div class="cap" style="background:var(--blue)"><h4>LAWN MOWER</h4><p>Lorem ipsum dolor sit amet,<br>consectetur adipiscing elit. Aliquam</p><span class="go"></span></div>
  </div>
  <div class="abs tile" style="left:394px">
    <div class="img" role="img" aria-label="Garden spade and fork in soil under blue sky" style="background:linear-gradient(180deg,#a9c6e6,#7a9a5a 70%,#5a4a34)"></div>
    <div class="cap" style="background:var(--green)"><h4>GARDENING TOOLS</h4><p>Lorem ipsum dolor sit amet,<br>consectetur adipiscing elit. Aliquam</p><span class="go"></span></div>
  </div>
  <div class="abs tile" style="left:543px">
    <div class="img" role="img" aria-label="String trimmer on lawn" style="background:linear-gradient(135deg,#9bc455,#6c9a34)"></div>
    <div class="cap" style="background:var(--dark)"><h4>STRING TRIMMER</h4><p>Lorem ipsum dolor sit amet,<br>consectetur adipiscing elit. Aliquam</p><span class="go"></span></div>
  </div>

  <div class="abs sec-head" style="top:510px">FEATURED PRODUCTS</div>

  <div class="abs card" style="left:244px;top:547px">
    <div class="img" role="img" aria-label="Red push lawn mower" style="background:radial-gradient(circle at 60% 60%,#e4b0ad,#fff 60%)"><div class="price">€34<small>.95</small> <s>37.00</s></div></div>
    <h5>Lorem ipsum dolor sit consectetur adipis.</h5>
    <p>Lorem ipsum dolor sit amet conse ctetur adipisicing elit, sed do eiusmod tempor incididunt</p>
    <div class="actions"><span class="add">ADD TO CART</span><span class="ic"><svg width="8" height="7"><path d="M1 7V4M3 7V2M5 7V3M7 7V1" stroke="#bbb"/></svg></span><span class="ic"><svg width="8" height="8" viewBox="0 0 10 10"><path d="M5 0l1.5 3.3 3.5.3-2.7 2.3.9 3.5L5 7.5 1.8 9.4l.9-3.5L0 3.6l3.5-.3z" fill="#ccc"/></svg></span></div>
  </div>
  <div class="abs card" style="left:394px;top:547px">
    <div class="img" role="img" aria-label="Green watering can" style="background:radial-gradient(circle at 55% 50%,#bcd98a,#fff 60%)"><div class="price">€34<small>.95</small> <s>37.00</s></div></div>
    <h5>Lorem ipsum dolor sit consectetur adipis.</h5>
    <p>Lorem ipsum dolor sit amet conse ctetur adipisicing elit, sed do eiusmod tempor incididunt</p>
    <div class="actions"><span class="add on">ADD TO CART</span><span class="ic"><svg width="8" height="7"><path d="M1 7V4M3 7V2M5 7V3M7 7V1" stroke="#bbb"/></svg></span><span class="ic"><svg width="8" height="8" viewBox="0 0 10 10"><path d="M5 0l1.5 3.3 3.5.3-2.7 2.3.9 3.5L5 7.5 1.8 9.4l.9-3.5L0 3.6l3.5-.3z" fill="#ccc"/></svg></span></div>
  </div>
  <div class="abs card" style="left:543px;top:547px">
    <div class="img" role="img" aria-label="Hand trowel with soil and pink flowers" style="background:radial-gradient(circle at 60% 45%,#dcc2c8,#fff 55%)"><div class="price">€34<small>.95</small> <s>37.00</s></div></div>
    <h5>Lorem ipsum dolor sit consectetur adipis.</h5>
    <p>Lorem ipsum dolor sit amet conse ctetur adipisicing elit, sed do eiusmod tempor incididunt</p>
    <div class="actions"><span class="add">ADD TO CART</span><span class="ic"><svg width="8" height="7"><path d="M1 7V4M3 7V2M5 7V3M7 7V1" stroke="#bbb"/></svg></span><span class="ic"><svg width="8" height="8" viewBox="0 0 10 10"><path d="M5 0l1.5 3.3 3.5.3-2.7 2.3.9 3.5L5 7.5 1.8 9.4l.9-3.5L0 3.6l3.5-.3z" fill="#ccc"/></svg></span></div>
  </div>

  <div class="abs offer">
    <div class="abs art1" role="img" aria-label="Basket of garden tools"></div>
    <h2 class="abs"><em>Minaru</em> SPECIAL OFFER</h2>
    <div class="abs sub">Limited Time Offer 1 Jan to 15 Jan</div>
    <div class="abs btn">GET OFFER</div>
    <div class="abs art2" role="img" aria-label="Trowel with seedling in soil"></div>
  </div>

  <div class="abs card" style="left:244px;top:848px">
    <div class="img" role="img" aria-label="Terracotta pots with flowers and bulbs" style="background:radial-gradient(circle at 50% 60%,#dba47c,#fff 60%)"><div class="price">€34<small>.95</small> <s>37.00</s></div></div>
    <h5>Lorem ipsum dolor sit consectetur adipis.</h5>
    <p>Lorem ipsum dolor sit amet conse ctetur adipisicing elit, sed do eiusmod tempor incididunt</p>
    <div class="actions"><span class="add">ADD TO CART</span><span class="ic"><svg width="8" height="7"><path d="M1 7V4M3 7V2M5 7V3M7 7V1" stroke="#bbb"/></svg></span><span class="ic"><svg width="8" height="8" viewBox="0 0 10 10"><path d="M5 0l1.5 3.3 3.5.3-2.7 2.3.9 3.5L5 7.5 1.8 9.4l.9-3.5L0 3.6l3.5-.3z" fill="#ccc"/></svg></span></div>
  </div>
  <div class="abs card" style="left:394px;top:848px">
    <div class="img" role="img" aria-label="Wooden seedling crate with small pots" style="background:radial-gradient(circle at 50% 60%,#c9a474,#fff 60%)"><div class="price">€34<small>.95</small> <s>37.00</s></div></div>
    <h5>Lorem ipsum dolor sit consectetur adipis.</h5>
    <p>Lorem ipsum dolor sit amet conse ctetur adipisicing elit, sed do eiusmod tempor incididunt</p>
    <div class="actions"><span class="add">ADD TO CART</span><span class="ic"><svg width="8" height="7"><path d="M1 7V4M3 7V2M5 7V3M7 7V1" stroke="#bbb"/></svg></span><span class="ic"><svg width="8" height="8" viewBox="0 0 10 10"><path d="M5 0l1.5 3.3 3.5.3-2.7 2.3.9 3.5L5 7.5 1.8 9.4l.9-3.5L0 3.6l3.5-.3z" fill="#ccc"/></svg></span></div>
  </div>
  <div class="abs card" style="left:543px;top:848px">
    <div class="img" role="img" aria-label="Green wheelbarrow" style="background:radial-gradient(circle at 45% 45%,#b8d67a,#fff 60%)"><div class="price">€34<small>.95</small> <s>37.00</s></div></div>
    <h5>Lorem ipsum dolor sit consectetur adipis.</h5>
    <p>Lorem ipsum dolor sit amet conse ctetur adipisicing elit, sed do eiusmod tempor incididunt</p>
    <div class="actions"><span class="add">ADD TO CART</span><span class="ic"><svg width="8" height="7"><path d="M1 7V4M3 7V2M5 7V3M7 7V1" stroke="#bbb"/></svg></span><span class="ic"><svg width="8" height="8" viewBox="0 0 10 10"><path d="M5 0l1.5 3.3 3.5.3-2.7 2.3.9 3.5L5 7.5 1.8 9.4l.9-3.5L0 3.6l3.5-.3z" fill="#ccc"/></svg></span></div>
  </div>
</main>

<footer>
  <div class="abs footer">
    <div class="fcol" style="left:17px"><h6>INFORMATION</h6><ul><li>What's New?</li><li>Products</li><li>About us</li><li>AGB</li><li>Impressum</li></ul></div>
    <div class="fcol" style="left:122px"><h6>WHY BUY FROM US</h6><ul><li>Shipping &amp; Returns</li><li>Secure Shopping</li><li>Top sellers</li><li>Gifts</li><li>Garden Tips</li></ul></div>
    <div class="fcol" style="left:242px"><h6>MY ACCOUNT</h6><ul><li>My Account</li><li>Order History</li><li>Wish List</li><li>Sign in</li><li>Newsletter</li></ul></div>
    <div class="fcol social" style="left:340px"><h6>FOLLOW US</h6><ul><li>Circlenet</li><li>Friendbook</li><li>Chirper</li><li>Viewtube</li></ul></div>
    <div class="fcol contact" style="left:430px"><h6>CONTACT US</h6>
      <p>comapany address, comapany address<br>comapany address</p>
      <p>Phone: <b>00031 55501 42</b></p>
      <p>Support: <b>hallo@minaru.de</b></p>
    </div>
  </div>
  <div class="abs bottom">
    <span>MINARU © 2013 &nbsp;Privacy Policy &nbsp;| &nbsp;Terms &amp; conditions</span>
    <span class="pm">Payment method: <b>Pelvanto</b><b>Crestiva</b><b>Kartilo</b><b>Brivalto</b></span>
  </div>
</footer>
</body>
</html>
```